Designing a website that functions as the shop window for the various aspects of my business -...

I need a website, with separate webpages covering the different components of my practice (small animal consultancy, equine behaviour consultancy, legal case work and education provider). I have a website (www.petmindstudio.ie) but I haven't updated it in recent years to reflect the newer developments / aspects of my business. Most of my work has been in Ireland but I would like to begin to create an international profile, particularly with regard to the legal casework and offering education within the international horse industry. My overall goal is to improve understanding of animals and animal behaviour, and by doing so, help to reduce the performance of behaviour problems, and also improve animal welfare as a result.

Target Market(s)

Horse and dog owners, horse riders, veterinary surgeons, solicitors

Industry/Entity Type

Legal

Logo Text

Text to be decided on

Number of Pages Required

5+ page

Font styles to use
Sans Serif
Decorative
Script

Colors

Designer to choose colors to be used in the design.

Requirements
Must have
• Relevant content from the attached Flyer including photos
• Use of the phrases:
• 'Understanding Animals'
• Improving animals lives through better understanding
• Science-based, up-to-date relevant information regarding animal behaviour
Nice to have
• 'Leading professional service educating people in understanding animals'
• Separate pages for 1) About, 2) Canine and Feline behaviour Consultancy 3) Equine Consultancy 4) Legal expert witness Consultancy 5) Education 6, FAQs
Should not have
• Prices of services (as these may change from time to time)

```html
<!DOCTYPE html>
<html lang="en">
<head>
<meta charset="utf-8">
<title>PetMind Studio</title>
<link href="https://fonts.googleapis.com/css2?family=Lato:wght@400;700;900&display=swap" rel="stylesheet">
<style>
:root{
  --green:#15964a;
  --green-dark:#0f7a3c;
  --green-light:#34c46e;
  --ink:#1c1c1c;
  --text:#3a3a3a;
  --muted:#8a8a8a;
  --mint:#e6f4f3;
  --white:#ffffff;
}
*{box-sizing:border-box;margin:0;padding:0}
html,body{width:1200px;height:3000px;overflow:hidden;background:var(--white);font-family:'Lato',sans-serif;color:var(--text)}
.page{position:relative;width:1200px;height:3000px}
.abs{position:absolute}

/* header */
.brand{left:80px;top:34px;display:flex;align-items:center;gap:14px}
.brand-mark{width:30px;height:30px;border-radius:50%;background:var(--green)}
.brand-name{font-family:'Lato',sans-serif;font-weight:900;font-size:38px;color:var(--green)}
.top-links{right:160px;top:10px;font-size:14px;color:var(--ink);display:flex;gap:10px}
.main-nav{left:535px;top:44px;display:flex;font-size:17px;font-weight:700;color:var(--ink);line-height:1.3}
.main-nav span{display:block}
.main-nav .n1{width:222px}.main-nav .n2{width:138px}

/* hero */
.hero{left:0;top:115px;width:1200px;height:615px;background:linear-gradient(160deg,#8aa86a 0%,#5f7f45 40%,#3d5a30 75%,#2b4424 100%)}
.hero-title{left:0;top:318px;width:1200px;text-align:center;color:var(--white);font-weight:900;font-size:40px;line-height:52px;text-transform:uppercase}
.btn-solid{background:var(--green);color:var(--white);font-weight:900;font-size:18px;text-align:center;text-transform:uppercase}
.hero-btn{left:495px;top:445px;width:176px;height:50px;line-height:50px}
.arrow{width:56px;height:56px}

/* components */
.comp-band{left:145px;top:645px;width:935px;height:150px;background:linear-gradient(90deg,var(--green-dark),var(--green-light))}
.comp-intro{left:145px;top:645px;width:260px;height:265px;background:linear-gradient(180deg,var(--green) 55%,rgba(255,255,255,0) 100%)}
.comp-title{left:187px;top:703px;color:var(--white);font-weight:900;font-size:28px}
.comp-text{left:190px;top:748px;width:196px;color:var(--white);font-size:19px;line-height:22px}
.card{top:688px;width:203px;height:310px;overflow:hidden}
.card-label{position:absolute;left:28px;bottom:40px;color:var(--white);font-weight:900;font-size:17px;line-height:20px}
.card-rule{position:absolute;left:28px;bottom:28px;width:34px;height:3px;background:var(--white)}

.vline{width:2px;background:var(--green)}
.dot{width:16px;height:16px;border:2px solid var(--green);border-radius:50%;background:var(--white)}

/* understanding */
.u-title{left:145px;top:1152px;font-weight:900;font-size:31px;color:var(--ink);text-transform:uppercase}
.u-text{left:147px;top:1210px;width:390px;font-size:16px;line-height:23px}
.u-text p{margin-bottom:22px}
.btn-outline{border:3px solid var(--green);color:var(--green);font-weight:900;text-align:center;text-transform:uppercase;background:var(--white)}
.u-btn{left:150px;top:1400px;width:176px;height:52px;line-height:46px;font-size:18px}
.u-photo{left:584px;top:1145px;width:460px;height:307px;background:linear-gradient(135deg,#d8b06a,#b88a4a 50%,#6f8a5a)}

/* offer */
.offer{left:0;top:1570px;width:1200px;height:548px;background:linear-gradient(135deg,var(--green-light) 0%,var(--green) 55%,var(--green-dark) 100%)}
.offer-title{left:0;top:1665px;width:1200px;text-align:center;color:var(--white);font-weight:900;font-size:29px;text-transform:uppercase}
.svc{top:1725px;width:190px;color:var(--white)}
.svc-icon{width:90px;height:90px;border-radius:50%;background:var(--green-dark);display:flex;align-items:center;justify-content:center}
.svc-name{margin-top:30px;font-weight:900;font-size:19px;line-height:23px;height:52px}
.svc-rule{margin-top:8px;width:38px;height:3px;background:var(--white)}
.svc-text{margin-top:18px;font-size:14px;line-height:18px;width:175px}
.svc-btn{margin-top:18px;width:128px;height:36px;line-height:32px;border:2px solid var(--white);color:var(--white);font-weight:900;font-size:12px;text-align:center;text-transform:uppercase}

/* science */
.sci{left:0;top:2118px;width:1200px;height:495px;background:var(--mint)}
.sci-photo{left:0;top:2118px;width:660px;height:495px;background:linear-gradient(90deg,#7a4a2a 0%,#9a6a45 40%,#b89a7a 75%,rgba(230,244,243,0) 100%)}
.sci-title{left:613px;top:2215px;width:480px;font-weight:900;font-size:27px;line-height:33px;color:var(--ink);text-transform:uppercase}
.sci-text{left:615px;top:2330px;width:400px;font-size:16px;line-height:23px}
.sci-btn{left:615px;top:2452px;width:176px;height:52px;line-height:46px;font-size:18px}

/* footer */
.f-logo{left:190px;top:2700px;width:64px;height:64px;border-radius:50%;background:var(--green)}
.f-col{top:2680px;font-size:14px;color:var(--ink)}
.f-col h4{font-weight:900;font-size:16px;text-transform:uppercase;margin-bottom:22px}
.f-row{display:flex;align-items:flex-start;gap:14px;margin-bottom:16px;line-height:18px}
.f-list li{list-style:none;margin-bottom:9px;line-height:17px}
.f-social .f-row{align-items:center;margin-bottom:14px}
.soc{width:24px;height:24px;border-radius:50%;background:var(--green);flex:none}
.f-line{left:0;top:2925px;width:1200px;height:1px;background:#dcdcdc}
.copy{left:0;top:2945px;width:1200px;text-align:center;font-size:14px;color:var(--muted)}
</style>
</head>
<body>
<div class="page">

  <header>
    <div class="abs brand"><span class="brand-mark"></span><span class="brand-name">PetMind Studio</span></div>
    <nav class="abs top-links"><span>About</span><span>|</span><span>Education</span><span>|</span><span>Contact us</span></nav>
    <nav class="abs main-nav">
      <span class="n1">Canine and Feline<br>behaviour Consultancy</span>
      <span class="n2">Equine<br>Consultancy</span>
      <span>Legal expert witness<br>Consultancy</span>
    </nav>
  </header>

  <section>
    <div class="abs hero" role="img" aria-label="Dog sitting on grass looking up at a trainer's raised hand"></div>
    <svg class="abs arrow" style="left:96px;top:384px" viewBox="0 0 56 56"><circle cx="28" cy="28" r="28" fill="rgba(255,255,255,.75)"/><path d="M32 19 L23 28 L32 37" stroke="#222" stroke-width="3" fill="none"/></svg>
    <svg class="abs arrow" style="left:1040px;top:384px" viewBox="0 0 56 56"><circle cx="28" cy="28" r="28" fill="rgba(255,255,255,.75)"/><path d="M24 19 L33 28 L24 37" stroke="#222" stroke-width="3" fill="none"/></svg>
    <h1 class="abs hero-title">Improving animals lives<br>through better understanding</h1>
    <div class="abs btn-solid hero-btn">Read more</div>
  </section>

  <section>
    <div class="abs comp-band"></div>
    <div class="abs comp-intro"></div>
    <h2 class="abs comp-title">COMPONENTS</h2>
    <p class="abs comp-text">Pellentesque faucibus Ut accumsan ultricies elit Maecenas</p>
    <div class="abs card" style="left:405px;background:linear-gradient(180deg,#9ac070,#e8d8b0 50%,#3a5a2a 85%,#111)" role="img" aria-label="Labrador lying on grass">
      <span class="card-label">Small Animal<br>Consultancy</span><span class="card-rule"></span>
    </div>
    <div class="abs card" style="left:623px;background:linear-gradient(180deg,#3a3a30,#6a5a4a 50%,#2a2a24 85%,#111)" role="img" aria-label="Girl in riding helmet with a dark horse">
      <span class="card-label">Equine Behaviour<br>Consultancy</span><span class="card-rule"></span>
    </div>
    <div class="abs card" style="left:845px;background:linear-gradient(180deg,#b0b0a8,#7a766e 50%,#3a3834 85%,#111)" role="img" aria-label="Close-up of a tabby cat">
      <span class="card-label">Legal case work and<br>Education provider</span><span class="card-rule"></span>
    </div>
    <div class="abs vline" style="left:297px;top:890px;height:228px"></div>
    <div class="abs dot" style="left:290px;top:1116px"></div>
  </section>

  <section>
    <h2 class="abs u-title">Understanding Animals</h2>
    <div class="abs u-text">
      <p>Pellentesque faucibus Ut accumsan ultricies elit Maecenas at justo id velit placerat molestie</p>
      <p>Donec dictum lectus non odio Cras a ante vitae enim iaculis aliquam Mauris nunc quam venenatis nec euismod sit amet egestas placerat est Pellentesque habitant morbi tristique senectus et netus</p>
    </div>
    <div class="abs btn-outline u-btn">Read more</div>
    <svg class="abs" style="left:560px;top:1280px" width="275" height="200" viewBox="0 0 275 200"><polygon points="0,0 25,0 25,172 275,172 245,198 0,198" fill="var(--green)"/></svg>
    <div class="abs u-photo" role="img" aria-label="Smiling man hugging a golden dog in a sunny field"></div>
    <div class="abs vline" style="left:599px;top:1478px;height:166px"></div>
  </section>

  <section>
    <svg class="abs" style="left:0;top:1555px" width="1200" height="20" viewBox="0 0 1200 20" preserveAspectRatio="none"><path d="M0 18 L40 12 L90 16 L140 9 L200 14 L260 8 L330 13 L400 7 L470 12 L540 9 L610 14 L680 8 L750 13 L820 7 L890 12 L960 9 L1030 14 L1100 8 L1160 12 L1200 10 L1200 20 L0 20 Z" fill="var(--green-light)"/></svg>
    <div class="abs offer"></div>
    <div class="abs dot" style="left:592px;top:1636px;border-color:var(--white);background:transparent"></div>
    <h2 class="abs offer-title">What we offer</h2>

    <div class="abs svc" style="left:158px">
      <div class="svc-icon"><svg width="46" height="46" viewBox="0 0 46 46" fill="none" stroke="#fff" stroke-width="2.5"><path d="M8 36 L8 24 L20 24 L28 12 L34 14 L38 20 L32 22 L30 36 M14 36 L14 28"/></svg></div>
      <div class="svc-name">Behaviour<br>Consultations</div><div class="svc-rule"></div>
      <p class="svc-text">Pellentesque faucibus Ut accumsan ultricies elit Maecenas at justo id velit placerat molestie</p>
      <div class="svc-btn">Read more</div>
    </div>
    <div class="abs svc" style="left:373px">
      <div class="svc-icon"><svg width="46" height="46" viewBox="0 0 46 46" fill="none" stroke="#fff" stroke-width="3"><path d="M6 14 H40 M12 14 L8 36 M34 14 L38 36 M12 14 V20 H34 V14"/></svg></div>
      <div class="svc-name">Training<br>Sessions</div><div class="svc-rule"></div>
      <p class="svc-text">Pellentesque faucibus Ut accumsan ultricies elit Maecenas at justo id velit placerat molestie</p>
      <div class="svc-btn">Read more</div>
    </div>
    <div class="abs svc" style="left:595px;width:210px">
      <div class="svc-icon"><svg width="46" height="46" viewBox="0 0 46 46" fill="none" stroke="#fff" stroke-width="2.5"><path d="M14 40 L20 26 L16 16 L24 6 L32 10 L30 16 L26 18 L30 30 L26 40"/></svg></div>
      <div class="svc-name">Training your horse<br>theory and practice</div><div class="svc-rule"></div>
      <p class="svc-text">Pellentesque faucibus Ut accumsan ultricies elit Maecenas at justo id velit placerat molestie</p>
      <div class="svc-btn">Read more</div>
    </div>
    <div class="abs svc" style="left:835px;width:230px">
      <div class="svc-icon"><svg width="46" height="46" viewBox="0 0 46 46" fill="none" stroke="#fff" stroke-width="2.5"><circle cx="23" cy="23" r="15"/><path d="M16 20 L23 30 L30 20"/></svg></div>
      <div class="svc-name">Training, performance<br>and welfare</div><div class="svc-rule"></div>
      <p class="svc-text">Pellentesque faucibus Ut accumsan ultricies elit Maecenas at justo id velit placerat molestie</p>
      <div class="svc-btn">Read more</div>
    </div>
  </section>

  <section>
    <div class="abs sci"></div>
    <div class="abs sci-photo" role="img" aria-label="Young woman standing beside a bay horse"></div>
    <h2 class="abs sci-title">Science-based, up-to-date<br>relevant information<br>regarding animal behaviour</h2>
    <p class="abs sci-text">Donec dictum lectus non odio Cras a ante vitae enim iaculis aliquam Mauris nunc quam venenatis nec euismod sit amet egestas placerat est Pellentesque habitant morbi tristique senectus et netus</p>
    <div class="abs btn-outline sci-btn">Read more</div>
    <svg class="abs" style="left:0;top:2600px" width="1200" height="16" viewBox="0 0 1200 16" preserveAspectRatio="none"><path d="M0 16 L1200 16 L1200 6 L1140 10 L1080 5 L1010 11 L940 6 L870 12 L800 5 L730 10 L660 6 L590 12 L520 5 L450 11 L380 6 L310 12 L240 5 L170 10 L100 6 L40 11 L0 7 Z" fill="var(--white)"/></svg>
  </section>

  <footer>
    <div class="abs f-logo"></div>
    <div class="abs f-col" style="left:368px">
      <h4>Contact us</h4>
      <div class="f-row"><svg width="16" height="20" viewBox="0 0 16 20" fill="none" stroke="#222" stroke-width="1.6"><path d="M8 19 C3 12 1.5 9.5 1.5 7 A6.5 6.5 0 0 1 14.5 7 C14.5 9.5 13 12 8 19Z"/><circle cx="8" cy="7" r="2.3"/></svg><span>42 Meadow Lane, Unit 3<br>Kilbrook KB4 7TR</span></div>
      <div class="f-row"><svg width="16" height="16" viewBox="0 0 16 16" fill="none" stroke="#222" stroke-width="1.6"><path d="M3 1.5 L6 1.5 L7 5 L5 6.5 C6 8.5 7.5 10 9.5 11 L11 9 L14.5 10 L14.5 13 C14.5 14 13.5 14.5 12.5 14.5 C6.5 14 2 9.5 1.5 3.5 C1.5 2.5 2 1.5 3 1.5Z"/></svg><span>555.014.2280</span></div>
      <div class="f-row"><svg width="17" height="13" viewBox="0 0 17 13" fill="none" stroke="#222" stroke-width="1.6"><rect x="1" y="1" width="15" height="11"/><path d="M1 1 L8.5 7 L16 1"/></svg><span>hello@petmindstudio.ie</span></div>
    </div>
    <div class="abs f-col" style="left:636px">
      <h4>Company</h4>
      <ul class="f-list">
        <li>About</li>
        <li>Canine and Feline<br>behaviour Consultancy</li>
        <li>Equine Consultancy</li>
        <li>Legal expert witness Consultancy</li>
        <li>Education</li>
        <li>Contact us</li>
      </ul>
    </div>
    <div class="abs f-col f-social" style="left:907px">
      <h4>Get in touch</h4>
      <div class="f-row"><span class="soc"></span><span>News feed</span></div>
      <div class="f-row"><span class="soc"></span><span>Community</span></div>
      <div class="f-row"><span class="soc"></span><span>Network</span></div>
      <div class="f-row"><span class="soc"></span><span>Gallery</span></div>
    </div>
    <div class="abs f-line"></div>
    <p class="abs copy">Copyright © 2019 All right reserved</p>
  </footer>

</div>
</body>
</html>
```